Advertising brochure for Trail Along Southside

We need a new single sided DL flier for the 2020 season!<br/>This flier is for our tour business. You can find all the details about the tour at our web site http://trailalong.southside.example<br/>The flier needs to grab the tourists attention, explain the tour and give price. I will upload a copy of last year's flier for your reference.<br/>We'd like the flier to match our web site to some extent.<br/>The most up to date information is on the web site and NOT last year's brochure. Use the web site for tour itinerary. We NO LONGER do the "Orchard Walk".<br/>Remember the size is "DL". Please no A4 format etc.<br/>You will be able to source images from:<br/>- Our web site<br/>- Our Chatterbook<br/>- Roamreview<br/>- Quarrel Listings<br/>If you have a particular idea in mind then feel free to contact us and we will try to accommodate your photo request.<br/>Good luck!

Target Market(s)

All ages

Industry/Entity Type

Tourism

Requirements
Must have
• Phone number
• Web Site
• Email address
• Price
Nice to have
• Description of tour and images

```html
<!DOCTYPE html>
<html lang="en">
<head>
<meta charset="utf-8">
<title>Trail Along Southside – Tag-Along Tour Flier</title>
<link href="https://fonts.googleapis.com/css2?family=Work+Sans:wght@300;400;500;600;700;800;900&display=swap" rel="stylesheet">
<style>
  :root {
    --page-bg: #e3e3e3;
    --paper: #ffffff;
    --orange: #f68a0a;
    --ink: #1f1f1f;
    --white: #ffffff;
    --sand-light: #c9b5a3;
    --sand-mid: #ab9584;
    --sand-dark: #8f7a6a;
  }
  * { margin: 0; padding: 0; box-sizing: border-box; }
  html, body { width: 1200px; height: 1116px; overflow: hidden; background: var(--page-bg); }
  body { font-family: "Work Sans", Arial, sans-serif; position: relative; }

  .flier {
    position: absolute; left: 372px; top: 74px;
    width: 457px; height: 968px;
    background: var(--paper); overflow: hidden;
  }

  .hero { position: absolute; left: 0; top: 0; width: 457px; height: 432px; }
  .hero-photo {
    position: absolute; inset: 0;
    background:
      radial-gradient(ellipse at 70% 20%, rgba(210,195,180,0.6), transparent 60%),
      linear-gradient(160deg, var(--sand-light) 0%, var(--sand-mid) 55%, var(--sand-dark) 100%);
  }

  .price { position: absolute; left: 37px; top: 50px; color: var(--white); }
  .price-amount { font-size: 58px; font-weight: 800; line-height: 1; letter-spacing: -1px; }
  .price-amount .currency { font-weight: 300; font-size: 50px; }
  .price-unit { font-size: 15.5px; font-weight: 800; line-height: 1; margin-top: 2px; letter-spacing: -0.3px; }
  .price-note { font-size: 9.5px; font-weight: 700; line-height: 12px; margin-top: 2px; text-transform: uppercase; }

  .brand-badge {
    position: absolute; left: 239px; top: 26px;
    width: 192px; height: 192px; border-radius: 50%;
    background: var(--orange);
    display: flex; align-items: center; justify-content: center; text-align: center;
  }
  .brand-name { color: var(--white); font-size: 22px; font-weight: 700; line-height: 1.15; width: 140px; }

  .headline {
    position: absolute; left: 37px; top: 200px;
    color: var(--white); font-size: 31px; font-weight: 900;
    line-height: 28px; text-transform: uppercase; letter-spacing: -0.6px;
  }
  .intro {
    position: absolute; left: 37px; top: 350px; width: 400px;
    color: var(--white); font-size: 12.2px; font-weight: 600; line-height: 16.5px;
  }

  .feature { position: absolute; width: 115px; }
  .feature-photo { width: 110px; height: 110px; border-radius: 50%; }
  .feature-title {
    position: relative; margin-top: -8px;
    color: var(--orange); font-size: 13.8px; font-weight: 800; line-height: 13px; text-transform: uppercase;
    letter-spacing: -0.2px;
  }
  .feature-title span { background: var(--paper); padding-right: 3px; box-decoration-break: clone; -webkit-box-decoration-break: clone; }
  .feature-text { width: 106px; font-size: 8.5px; line-height: 11.2px; color: var(--ink); margin-top: 2px; }

  .col-1 { left: 37px; } .col-2 { left: 174px; } .col-3 { left: 311px; }
  .row-1 { top: 463px; } .row-2 { top: 682px; }

  .photo-underground { background: radial-gradient(circle at 45% 45%, #b9a890, #6e5b48 70%, #3e3226); }
  .photo-safety { background: radial-gradient(circle at 50% 45%, #a98a86, #5f4147 65%, #2f1c26); }
  .photo-opal { background: radial-gradient(circle at 50% 50%, #9fc6b8, #d8e2e6 45%, #eef0f2 75%); }
  .photo-drive { background: linear-gradient(180deg, #3d5a82 0%, #b9946c 35%, #c7a982 70%, #9b7b5b 100%); }
  .photo-noodling { background: radial-gradient(circle at 40% 45%, #ddd3c4, #b7a58f 60%, #6f6256); }
  .photo-cutting { background: radial-gradient(circle at 50% 50%, #c8c6c0, #6b2a18 45%, #2c0d06 80%); }

  .contact { position: absolute; left: 174px; top: 885px; color: var(--ink); }
  .contact-phone { font-size: 31px; font-weight: 800; line-height: 1; letter-spacing: -0.3px; }
  .contact-line { font-size: 8px; font-weight: 700; line-height: 10px; text-transform: uppercase; }
  .contact-phone + .contact-line { margin-top: 2px; }
</style>
</head>
<body>
  <main class="flier">
    <section class="hero">
      <div class="hero-photo" role="img" aria-label="Aerial photo of a convoy of cars driving along a dirt road through pale desert opal fields"></div>

      <div class="price">
        <div class="price-amount"><span class="currency">$</span>40</div>
        <div class="price-unit">PER PERSON</div>
        <div class="price-note">Kids half price,<br>children under 5 free!</div>
      </div>

      <div class="brand-badge">
        <div class="brand-name">Trail Along Southside</div>
      </div>

      <h1 class="headline">A unique<br>tag-along<br>journey<br>through<br>Coober Pedy</h1>
      <p class="intro">Enjoy a tour from the comfort of your<br>own car as our experienced guide takes<br>you through a “day in the life” of a coober pedy miner.</p>
    </section>

    <article class="feature col-1 row-1">
      <div class="feature-photo photo-underground" role="img" aria-label="Photo of a carved sandstone room inside an underground dugout home"></div>
      <h2 class="feature-title"><span>Underground<br>home</span></h2>
      <p class="feature-text">Our guide’s family open the doors of their home and give you a guided tour of their dugout. See how a modern family live underground.</p>
    </article>

    <article class="feature col-2 row-1">
      <div class="feature-photo photo-safety" role="img" aria-label="Photo of visitors wearing helmets in a mine"></div>
      <h2 class="feature-title"><span>Safety<br>gear</span></h2>
      <p class="feature-text">All safety gear will be provided for you including helmets and UHF radios. Your safety is our number one priority!</p>
    </article>

    <article class="feature col-3 row-1">
      <div class="feature-photo photo-opal" role="img" aria-label="Photo of a rough opal stone on a white background"></div>
      <h2 class="feature-title"><span>Opal<br>mining</span></h2>
      <p class="feature-text">We’ll make our way down an underground mine where we’ll show you the different techniques that modern miners use to extract this beautiful stone.</p>
    </article>

    <article class="feature col-1 row-2">
      <div class="feature-photo photo-drive" role="img" aria-label="Aerial photo of cars driving through the opal field landscape"></div>
      <h2 class="feature-title"><span>Drive<br>through<br>the field</span></h2>
      <p class="feature-text">Making our way into town, via the opal fields, you’ll get a front row seat for viewing our magical landscape that has been terraformed with over 100 years of mining. We might even pop into a few of Coober Pedy’s famous sights on our way!</p>
    </article>

    <article class="feature col-2 row-2">
      <div class="feature-photo photo-noodling" role="img" aria-label="Photo of a miner drilling into a pale rock wall"></div>
      <h2 class="feature-title"><span>Noodling</span></h2>
      <p class="feature-text">Next we hit the noodling field to try and find our own opal. With our expert guide showing you how to find opal you’ll be a pro in no time!</p>
    </article>

    <article class="feature col-3 row-2">
      <div class="feature-photo photo-cutting" role="img" aria-label="Close-up photo of a polished opal with colourful flashes"></div>
      <h2 class="feature-title"><span>Opal cutting<br>and polishing</span></h2>
      <p class="feature-text">We’ll finish up our tour with an opal cutting and polishing demonstration and who knows?... It might be your opal we cut and polish!</p>
    </article>

    <footer class="contact">
      <div class="contact-phone">08 5550 1427</div>
      <div class="contact-line">hello@trailalong.southside.example</div>
      <div class="contact-line">http://trailalong.southside.example</div>
    </footer>
  </main>
</body>
</html>
```